Waste Oil Filter collection & disposal

Basically I need a 1 page website for the business called Brenmoor Waste Solutions.
We are a environmental service provider and we collect and dispose of waste oil filters to protect the environment from hazardous waste oil products.

This is the link to our current website: www.brenmoorwaste.co.nz

we want it to look fresh and better than our current website. we may potentially look at getting a new logo designed and are open to ideas/designs if you have any.

Industry/Entity Type

Business

Logo Text

Brenmoor Waste Solutions

Number of Pages Required

1 page

Requirements
Must have
• same colours as current website.
• description of what service we provide please refer to leaflet attached

```html
<!DOCTYPE html>
<html lang="en">
<head>
<meta charset="utf-8">
<title>Brenmoor Waste Solutions Ltd</title>
<link rel="stylesheet" href="https://fonts.googleapis.com/css2?family=Open+Sans:wght@600;700&family=Mulish:wght@400;600;700&display=swap">
<style>
:root{
  --green:#5aab2f;
  --green-dark:#4b9427;
  --ink:#333333;
  --text:#666666;
  --grey-band:#efefef;
  --white:#ffffff;
  --dark:#333333;
  --footer-text:#e6e6e6;
}
*{box-sizing:border-box;margin:0;padding:0}
html,body{width:1200px;height:3087px;overflow:hidden}
body{position:relative;background:var(--white);font-family:"Mulish",sans-serif;color:var(--text)}
.abs{position:absolute}
.heading{font-family:"Open Sans",sans-serif;font-weight:700;font-size:27px;color:var(--ink);text-align:center;text-transform:uppercase;letter-spacing:.3px}
.heading span{color:var(--green)}

/* header */
.hero{position:absolute;left:0;top:0;width:1200px;height:720px;overflow:hidden}
.hero-photo{position:absolute;inset:0;background:linear-gradient(160deg,#8d9a96 0%,#b9c3bd 35%,#6f8a7c 65%,#a8b3ab 100%)}
.hero-veil{position:absolute;inset:0;background:rgba(255,255,255,.55)}
.topbar{position:absolute;left:0;top:0;width:1200px;height:124px;background:rgba(40,40,40,.88);border-bottom:3px solid var(--green)}
.brand{position:absolute;left:78px;top:0;width:272px;height:144px;background:var(--white);display:flex;align-items:center;justify-content:center;gap:10px;box-shadow:0 2px 6px rgba(0,0,0,.2)}
.brand-dot{width:22px;height:22px;border-radius:50%;background:var(--green);flex:none}
.brand-name{font-family:"Open Sans",sans-serif;font-weight:700;font-size:20px;line-height:1.15;color:var(--ink);text-transform:uppercase}
.phone{position:absolute;left:757px;top:22px;display:flex;align-items:center;gap:12px;color:var(--white);font-size:21px}
.socials{position:absolute;left:940px;top:16px;display:flex;gap:10px}
.socials i{display:block;width:40px;height:40px;border-radius:50%;background:#242424;border:1px solid #555}
.nav{position:absolute;top:86px;left:950px;display:flex;gap:36px;font-family:"Open Sans",sans-serif;font-weight:600;font-size:17px;color:var(--white)}
.hero-title{position:absolute;top:326px;width:1200px;text-align:center;font-family:"Open Sans",sans-serif;font-weight:700;font-size:46px;color:var(--ink)}
.hero-sub{position:absolute;top:398px;width:1200px;text-align:center;font-size:21px;line-height:32px;color:var(--ink)}
.hero-swoosh{position:absolute;left:0;top:590px}

/* about */
.about-title{top:752px;width:1200px}
.about-lead{top:796px;left:220px;width:760px;text-align:center;font-size:15.5px;line-height:27px}
.feature{position:absolute;top:887px;width:220px;text-align:center;font-size:15.5px;line-height:25px}
.feature .ring{width:84px;height:84px;border:2px solid var(--green);border-radius:50%;margin:0 auto 22px;display:flex;align-items:center;justify-content:center}

/* services */
.services{position:absolute;left:0;top:1136px;width:1200px;height:270px;background:var(--grey-band)}
.service{position:absolute;top:62px;width:520px;text-align:center}
.service .heading{font-size:27px}
.service h3{font-weight:400;font-size:22px;color:var(--ink);margin:20px 0 14px}
.service p{font-size:15.5px;line-height:26px}

/* process */
.process-title{top:1460px;width:1200px}
.step{position:absolute;width:54px;height:54px;border-radius:50%;background:var(--dark);border:4px solid var(--white);box-shadow:0 0 0 2px var(--dark);color:var(--white);font-family:"Open Sans",sans-serif;font-weight:700;font-size:22px;display:flex;align-items:center;justify-content:center}
.step-label{position:absolute;font-size:15.5px;color:var(--text)}
.filters{position:absolute;left:435px;top:1578px;width:330px;height:280px;border-radius:40%;background:radial-gradient(circle at 45% 50%,#5a5a5a 0%,#2b2b2b 55%,rgba(255,255,255,0) 72%)}

/* gallery */
.gallery{position:absolute;left:0;top:1980px;width:1200px;height:335px;background:var(--grey-band)}
.gallery .heading{position:absolute;top:56px;width:1200px}
.shot{position:absolute;top:113px;width:239px;height:154px}
.shot-1{left:78px;background:var(--green);display:flex;align-items:center;justify-content:center}
.shot-2{left:346px;background:linear-gradient(135deg,#4a4f6a,#8a8fa0 50%,#3d4253)}
.shot-3{left:613px;background:linear-gradient(180deg,#b5c2b8 0%,#cfd8d1 45%,#3f8f6a 70%,#6b6f6c 100%)}
.shot-4{left:883px;background:linear-gradient(135deg,#51645a,#8fa59a 50%,#3e4d46)}
.arrow{position:absolute;top:170px}

/* testimonials */
.testi-title{top:2361px;width:1200px}
.quote{position:absolute;top:2428px;display:flex;gap:38px}
.quote .qmark{width:70px;height:70px;border:2px solid var(--green);border-radius:50%;display:flex;align-items:center;justify-content:center;flex:none;font-family:"Open Sans",sans-serif;font-weight:700;font-size:46px;color:var(--green);line-height:1}
.quote p{font-size:15.5px;line-height:25px;width:420px}
.quote cite{display:block;font-style:normal;font-weight:700;font-size:19px;color:var(--green);margin-top:8px}
.dots{position:absolute;top:2579px;left:549px;display:flex;gap:8px}
.dots i{display:block;width:26px;height:4px;background:#d6d6d6}
.dots i.on{background:var(--green)}

/* footer */
.footer-wave{position:absolute;left:0;top:2595px}
.footer{position:absolute;left:0;top:2700px;width:1200px;height:325px;background:var(--dark);color:var(--footer-text)}
.col{position:absolute;top:106px}
.col h4{font-family:"Open Sans",sans-serif;font-weight:700;font-size:21px;color:var(--white);text-transform:uppercase;margin-bottom:22px}
.col p{font-size:15.5px;line-height:29px}
.price{display:flex;gap:12px;font-size:15.5px;line-height:25px;margin-bottom:16px;width:200px}
.price b{flex:none;width:13px;height:13px;border-radius:50%;background:var(--green);margin-top:6px}
.contact{display:flex;align-items:center;gap:18px;font-size:15.5px;margin-bottom:14px}
.map{width:218px;height:100px;background:linear-gradient(160deg,#e8ecef 0%,#dfe5e9 55%,#cbdbe6 100%);border-radius:3px}
.legal{position:absolute;left:0;top:3025px;width:1200px;height:62px;background:var(--green);color:var(--ink);font-size:15.5px;text-align:center;line-height:62px}
</style>
</head>
<body>

<header class="hero">
  <div class="hero-photo" role="img" aria-label="Recycling plant interior with conveyor and stacked crushed metal"></div>
  <div class="hero-veil"></div>
  <div class="topbar">
    <div class="brand"><i class="brand-dot"></i><span class="brand-name">Brenmoor Waste<br>Solutions Ltd</span></div>
    <div class="phone">
      <svg width="20" height="20" viewBox="0 0 24 24"><path fill="#5aab2f" d="M6.6 10.8a15.1 15.1 0 0 0 6.6 6.6l2.2-2.2a1 1 0 0 1 1-.25 11.4 11.4 0 0 0 3.6.57 1 1 0 0 1 1 1V20a1 1 0 0 1-1 1A17 17 0 0 1 3 4a1 1 0 0 1 1-1h3.5a1 1 0 0 1 1 1c0 1.25.2 2.45.57 3.57a1 1 0 0 1-.25 1z"/></svg>
      06 555 0142
    </div>
    <div class="socials"><i></i><i></i><i></i><i></i></div>
    <nav class="nav"><span>ABOUT</span><span>GALLARY</span></nav>
  </div>
  <h1 class="hero-title">Brenmoor Waste Solutions Ltd</h1>
  <p class="hero-sub">specialize in the collection &amp; disposal of oil / fuel filters,<br>servicing the lower north island on a monthly cycle.</p>
  <svg class="hero-swoosh" width="1200" height="130" viewBox="0 0 1200 130">
    <path fill="#ffffff" d="M0 130 C300 70 700 20 1200 40 L1200 130 Z"/>
    <path fill="#5aab2f" d="M440 112 C650 30 950 0 1200 30 L1200 60 C950 35 700 45 440 112 Z"/>
  </svg>
</header>

<section>
  <h2 class="abs heading about-title">About <span>Us</span></h2>
  <p class="abs about-lead">We offer a cost effective environmentally friendly system for the collection and disposal of waste oil filters helping minimise contamination of landfills keeping your industry compliant.</p>
  <div class="feature" style="left:90px">
    <div class="ring"><svg width="40" height="40" viewBox="0 0 40 40"><path fill="#5aab2f" d="M20 4 L30 20 H24 L20 13 L16 20 H10 Z M6 26 H18 V34 H10 Z M34 26 L30 34 H22 V26 Z"/></svg></div>
    We are passionate about doing our bit in keeping New Zealand Clean and Green
  </div>
  <div class="feature" style="left:359px">
    <div class="ring"><svg width="40" height="40" viewBox="0 0 40 40"><circle cx="20" cy="20" r="15" fill="none" stroke="#5aab2f" stroke-width="3"/><path d="M5 20 H35 M20 5 V35" stroke="#5aab2f" stroke-width="2.5"/></svg></div>
    Our processes are environmentally friendly and minimise the contamination of landfills.
  </div>
  <div class="feature" style="left:627px">
    <div class="ring"><svg width="40" height="40" viewBox="0 0 40 40"><circle cx="20" cy="20" r="15" fill="#5aab2f"/><circle cx="20" cy="20" r="7" fill="#ffffff"/></svg></div>
    We offer a cost effective system for the collection and disposal of waste oil filters
  </div>
  <div class="feature" style="left:896px">
    <div class="ring"><svg width="40" height="40" viewBox="0 0 40 40"><path fill="#5aab2f" d="M6 34 V10 H12 V22 L20 16 V22 L28 16 V22 L34 16 V34 Z"/></svg></div>
    We keep your industry compliant.
  </div>
</section>

<section class="services">
  <div class="service" style="left:53px">
    <h2 class="heading">Service We <span>Provide</span></h2>
    <h3>Brenmoor Waste Service</h3>
    <p>Brenmoor Waste Solutions Ltd service the Lower North Island and<br>specialise in the collection &amp; disposal of oil &amp; fuel filters</p>
  </div>
  <div class="service" style="left:619px">
    <h2 class="heading">What Happens <span>To The Oil</span></h2>
    <h3>Oil Recycling</h3>
    <p>All residual oil is collected into our tank and then recycled.<br>Currently we are processing over 2,000 litres of oil a month</p>
  </div>
</section>

<section>
  <h2 class="abs heading process-title">Our <span>Process</span></h2>
  <svg class="abs" style="left:399px;top:1518px" width="400" height="400" viewBox="0 0 400 400">
    <circle cx="200" cy="200" r="196" fill="none" stroke="#5aab2f" stroke-width="2"/>
    <circle cx="200" cy="200" r="154" fill="none" stroke="#cfe7c2" stroke-width="2"/>
  </svg>
  <div class="filters" role="img" aria-label="Two black automotive oil filters"></div>
  <div class="step" style="left:426px;top:1562px">06</div>
  <div class="step" style="left:726px;top:1562px">01</div>
  <div class="step" style="left:372px;top:1693px">05</div>
  <div class="step" style="left:769px;top:1693px">02</div>
  <div class="step" style="left:436px;top:1821px">04</div>
  <div class="step" style="left:714px;top:1821px">03</div>
  <span class="step-label" style="left:282px;top:1578px">Metal Recycling</span>
  <span class="step-label" style="left:808px;top:1578px">Drained</span>
  <span class="step-label" style="left:224px;top:1710px">Drained 3rd time</span>
  <span class="step-label" style="left:852px;top:1710px">Sorted</span>
  <span class="step-label" style="left:277px;top:1842px">Crushed into bricks</span>
  <span class="step-label" style="left:792px;top:1842px">Drained again</span>
</section>

<section class="gallery">
  <h2 class="heading">Our <span>Gallery</span></h2>
  <svg class="arrow" style="left:46px" width="14" height="28" viewBox="0 0 14 28"><path d="M12 2 L3 14 L12 26" fill="none" stroke="#5aab2f" stroke-width="2.5"/></svg>
  <div class="shot shot-1" role="img" aria-label="Plant machinery with green highlight overlay">
    <svg width="48" height="48" viewBox="0 0 48 48"><circle cx="20" cy="20" r="13" fill="none" stroke="#fff" stroke-width="3.5"/><path d="M30 30 L42 42 M20 13 V27 M13 20 H27" stroke="#fff" stroke-width="3.5" stroke-linecap="round"/></svg>
  </div>
  <div class="shot shot-2" role="img" aria-label="Bins stacked with used oil filters"></div>
  <div class="shot shot-3" role="img" aria-label="Green and white collection truck"></div>
  <div class="shot shot-4" role="img" aria-label="Filter processing equipment"></div>
  <svg class="arrow" style="left:1136px" width="14" height="28" viewBox="0 0 14 28"><path d="M2 2 L11 14 L2 26" fill="none" stroke="#5aab2f" stroke-width="2.5"/></svg>
</section>

<section>
  <h2 class="abs heading testi-title">Our <span>Testimonials</span></h2>
  <div class="quote" style="left:78px">
    <div class="qmark">&#8220;</div>
    <div><p>each used oil filter has on aver age, more than quarter of a litre of used motor oil</p><cite>- EcoReturn Trust</cite></div>
  </div>
  <div class="quote" style="left:619px">
    <div class="qmark">&#8220;</div>
    <div><p>recycling engine oil protects the environment and conserves energy resources</p><cite>- Oil Recycling</cite></div>
  </div>
  <div class="dots"><i></i><i></i><i class="on"></i></div>
</section>

<svg class="footer-wave" width="1200" height="106" viewBox="0 0 1200 106">
  <path fill="#333333" d="M0 60 C350 150 800 120 1200 10 L1200 106 L0 106 Z"/>
  <path fill="#5aab2f" d="M480 92 C800 100 1050 50 1200 0 L1200 26 C1040 74 800 112 480 92 Z"/>
</svg>
<footer class="footer">
  <div class="col" style="left:78px">
    <h4>Opning Hours</h4>
    <p>Monday - Friday<br>7.30am - 5.00pm</p>
  </div>
  <div class="col" style="left:346px">
    <h4>Pricing</h4>
    <div class="price"><b></b><span>$65.00 - Monthly Bin Collection</span></div>
    <div class="price"><b></b><span>$35.00 - Additional Bins</span></div>
    <div class="price"><b></b><span>$85.00 - Account Set Up Fee</span></div>
  </div>
  <div class="col" style="left:613px">
    <h4>Contact Info</h4>
    <div class="contact"><svg width="20" height="20" viewBox="0 0 24 24"><path fill="#5aab2f" d="M6.6 10.8a15.1 15.1 0 0 0 6.6 6.6l2.2-2.2a1 1 0 0 1 1-.25 11.4 11.4 0 0 0 3.6.57 1 1 0 0 1 1 1V20a1 1 0 0 1-1 1A17 17 0 0 1 3 4a1 1 0 0 1 1-1h3.5a1 1 0 0 1 1 1c0 1.25.2 2.45.57 3.57a1 1 0 0 1-.25 1z"/></svg>info@brenmoorwaste.co.nz</div>
    <div class="contact"><svg width="20" height="16" viewBox="0 0 20 16"><rect x="1" y="1" width="18" height="14" fill="none" stroke="#5aab2f" stroke-width="2"/><path d="M1 1 L10 9 L19 1" fill="none" stroke="#5aab2f" stroke-width="2"/></svg>06 555 0142</div>
  </div>
  <div class="col" style="left:885px">
    <h4>Map</h4>
    <div class="map" role="img" aria-label="Street map showing the business location"></div>
  </div>
</footer>
<div class="legal">&copy;BRENMOOR WASTE SOLUTIONS LTD. 2017 - All Rights Reserved.</div>

</body>
</html>
```